PELMARK
stationery items
Professional
Karim Doulani
Managing Director
Corniva Plaza L27
Al Fannar Road
P.O. Box 58214
Dubai - UAE
kdoulani@pelmark-gulfa.com
www.pelmark-gulfa.com
looking for full stationery items (business cards, letter heads, envelopes)
LOGO
Strategic Advisory & Property Portfolio Management Services
full package of logo

```html
<!DOCTYPE html>
<html lang="en">
<head>
<meta charset="utf-8">
<title>Pelmark Stationery</title>
<link rel="stylesheet" href="https://fonts.googleapis.com/css2?family=Cormorant+Garamond:wght@500;600&display=swap">
<style>
:root{
  --backdrop:#e6e3de;
  --paper:#ffffff;
  --brand-red:#8c2a1e;
  --ink:#4a4a4a;
  --ink-soft:#808080;
  --rule:#d8d8d8;
  --shadow:0 4px 14px rgba(0,0,0,.14);
}
*{box-sizing:border-box;margin:0;padding:0}
html,body{width:1200px;height:816px;overflow:hidden}
body{background:var(--backdrop);font-family:"Cormorant Garamond",Georgia,serif;color:var(--ink);position:relative}
.piece{position:absolute;background:var(--paper);box-shadow:var(--shadow)}
.wordmark{display:flex;align-items:center;gap:7px;color:var(--brand-red);font-weight:600;letter-spacing:.06em;line-height:1}
.wordmark .mark-square{width:.55em;height:.55em;background:var(--ink)}
.wordmark.on-red{color:#fff}
.wordmark.on-red .mark-square{background:#fff}
.small{font-size:10px;line-height:1.35;color:var(--ink-soft);font-weight:500}
.tagline{font-size:12px;color:var(--ink);font-weight:500;padding:0 12px}

/* business cards */
.card{width:320px;height:183px}
.card-name{left:50px;top:60px}
.card-name .wordmark{position:absolute;left:26px;top:112px;font-size:24px}
.card-name .holder{position:absolute;left:176px;top:24px}
.holder .person{color:var(--brand-red);font-size:15px;font-weight:600}
.holder .role{font-size:10.5px;color:var(--ink-soft);margin-bottom:10px}
.card-logo{left:50px;top:300px}
.card-logo .wordmark,.card-red .wordmark{position:absolute;left:0;right:0;top:62px;justify-content:center;font-size:32px}
.card-logo .tagline,.card-red .tagline{position:absolute;left:0;right:0;top:112px;text-align:center}
.card-red{left:50px;top:540px;background:var(--brand-red)}
.card-red .tagline{color:#f3e6e3}

/* envelope */
.envelope{left:410px;top:150px;width:280px;height:140px}
.envelope .flap{position:absolute;inset:0}
.envelope .wordmark{position:absolute;left:0;right:0;top:70px;justify-content:center;font-size:22px}

/* compliment slip */
.comp-slip{left:410px;top:420px;width:280px;height:150px}
.comp-slip .wordmark{position:absolute;left:18px;top:20px;font-size:20px}
.comp-slip .address{position:absolute;left:18px;top:48px;font-size:8.5px}
.comp-slip .contacts{position:absolute;left:18px;bottom:14px;display:flex;gap:26px;font-size:8.5px}

/* letterhead */
.letterhead{left:730px;top:97px;width:440px;height:622px}
.letterhead .wordmark{position:absolute;left:34px;top:40px;font-size:26px}
.letterhead .address{position:absolute;left:34px;top:76px}
.letterhead .footer-rule{position:absolute;left:34px;right:34px;bottom:64px;height:1px;background:var(--rule)}
.letterhead .contacts{position:absolute;left:34px;bottom:30px;display:flex;gap:50px}
.bullet{display:inline-block;width:5px;height:5px;background:var(--brand-red);margin-right:5px;vertical-align:middle}
</style>
</head>
<body>

<section class="piece card card-name">
  <div class="holder">
    <div class="person">Karim Doulani</div>
    <div class="role">Managing Director</div>
    <div class="small">Corniva Plaza L27<br>Al Fannar Road<br>P.O. Box 58214, Dubai - UAE<br>T +971 4 555 0192<br>M +971 50 555 0148<br>kdoulani@pelmark-gulfa.com<br>www.pelmark-gulfa.com</div>
  </div>
  <div class="wordmark"><span class="mark-square"></span>PELMARK</div>
</section>

<section class="piece card card-logo">
  <div class="wordmark"><span class="mark-square"></span>PELMARK</div>
  <p class="tagline">Strategic Advisory &amp; Property Portfolio Management Services</p>
</section>

<section class="piece card card-red">
  <div class="wordmark on-red"><span class="mark-square"></span>PELMARK</div>
  <p class="tagline">Strategic Advisory &amp; Property Portfolio Management Services</p>
</section>

<section class="piece envelope">
  <svg class="flap" viewBox="0 0 280 140" aria-hidden="true">
    <polyline points="0,0 140,58 280,0" fill="none" stroke="#dcdcdc" stroke-width="1"/>
  </svg>
  <div class="wordmark"><span class="mark-square"></span>PELMARK</div>
</section>

<section class="piece comp-slip">
  <div class="wordmark"><span class="mark-square"></span>PELMARK</div>
  <div class="small address">Corniva Plaza L27, Al Fannar Road<br>P.O. Box 58214, Dubai - UAE</div>
  <div class="small contacts">
    <span>T +971 4 555 0192<br>F +971 4 555 0193</span>
    <span>kdoulani@pelmark-gulfa.com<br>www.pelmark-gulfa.com</span>
  </div>
</section>

<section class="piece letterhead">
  <div class="wordmark"><span class="mark-square"></span>PELMARK</div>
  <div class="small address">Corniva Plaza L27, Al Fannar Road<br>P.O. Box 58214, Dubai - UAE</div>
  <div class="footer-rule"></div>
  <div class="small contacts">
    <span><span class="bullet"></span>T +971 4 555 0192<br><span class="bullet"></span>F +971 4 555 0193</span>
    <span><span class="bullet"></span>kdoulani@pelmark-gulfa.com<br><span class="bullet"></span>www.pelmark-gulfa.com</span>
  </div>
</section>

</body>
</html>
```